Product Insert / Thank You

I'm looking for a small card to be designed that will be included with our product when it ships. It will be 2 sided with 1 side being a "thank you" with our logo and the other side containing the following text:We would love to hear your feedback! For every review we receive on our products, we donate 100% of the proceeds of your order to TIDEWELL -- a non profit organization dedicated to preserving our oceans!If you are not 100% satisfied with your purchase or have any problems, we will always resolve your issue. please contact us via Brindle if you need assistance.Insert needs to be well organized and information presented in a clear and visually appealing way.
Target Market(s)
Women, aged 24-45
Colors
Designer to choose colors to be used in the design.
Look and feel

```html
<!DOCTYPE html>
<html lang="en">
<head>
<meta charset="utf-8">
<title>Kestrel – Thank You Insert Card</title>
<link href="https://fonts.googleapis.com/css2?family=Playfair+Display:wght@500;600&family=Source+Sans+3:wght@400;700&display=swap" rel="stylesheet">
<style>
  :root {
    --page-bg: #ffffff;
    --dusty-blue: #8fabc2;
    --sand: #e2cfbe;
    --ink: #111111;
    --card-white: #ffffff;
    --card-shadow: rgba(0, 0, 0, 0.35);
  }
  * { box-sizing: border-box; margin: 0; padding: 0; }
  html, body {
    width: 1200px;
    height: 1200px;
    overflow: hidden;
    background: var(--page-bg);
  }
  .canvas {
    position: relative;
    width: 1200px;
    height: 1200px;
  }
  .card {
    position: absolute;
    width: 776px;
    height: 516px;
    box-shadow: 3px 4px 6px var(--card-shadow);
    overflow: hidden;
  }

  /* Front side */
  .card--front {
    left: 54px;
    top: 114px;
    background: var(--dusty-blue);
  }
  .card__split {
    position: absolute;
    inset: 0;
    width: 100%;
    height: 100%;
  }
  .brand-mark {
    position: absolute;
    left: 31px;
    top: 26px;
    width: 138px;
    height: 138px;
    border: 4px solid var(--ink);
    border-radius: 50%;
    display: flex;
    align-items: center;
    justify-content: center;
  }
  .brand-mark__name {
    font-family: "Playfair Display", serif;
    font-weight: 600;
    font-size: 19px;
    letter-spacing: 1.5px;
    color: var(--ink);
  }
  .front__title {
    position: absolute;
    left: 225px;
    top: 225px;
    font-family: "Playfair Display", serif;
    font-weight: 500;
    font-size: 72px;
    line-height: 1;
    letter-spacing: 0.5px;
    color: var(--ink);
    white-space: nowrap;
  }

  /* Back side */
  .card--back {
    left: 361px;
    top: 570px;
    background: var(--card-white);
  }
  .back__copy {
    position: absolute;
    left: 46px;
    top: 58px;
    width: 640px;
    font-family: "Source Sans 3", sans-serif;
    font-size: 19.5px;
    line-height: 27px;
    color: var(--ink);
  }
  .back__copy p + p { margin-top: 27px; }
  .back__copy strong { font-weight: 700; }
  .back__rule {
    position: absolute;
    left: 46px;
    top: 260px;
    width: 296px;
    height: 4px;
    background: var(--dusty-blue);
  }
  .back__headline {
    position: absolute;
    left: 0;
    right: 0;
    top: 370px;
    text-align: center;
    font-family: "Playfair Display", serif;
    font-weight: 600;
    font-size: 40px;
    line-height: 48px;
    letter-spacing: -0.5px;
    color: var(--ink);
  }
</style>
</head>
<body>
<main class="canvas">

  <section class="card card--front" aria-label="Front of insert card">
    <svg class="card__split" viewBox="0 0 776 516" preserveAspectRatio="none" aria-hidden="true">
      <polygon points="368,0 776,0 776,516 590,516" fill="var(--sand)"/>
    </svg>
    <div class="brand-mark">
      <span class="brand-mark__name">KESTREL</span>
    </div>
    <h1 class="front__title">THANK YOU</h1>
  </section>

  <section class="card card--back" aria-label="Back of insert card">
    <div class="back__copy">
      <p>For every review we receive on our products, we donate 100% of<br>
      the proceed of your order to “<strong>TIDEWELL</strong>” -&nbsp; a non profit<br>
      organization dedicated to preserving our oceans !</p>
      <p>If you’re not 100% satisfied with your purchase or have any<br>
      problems, we will always resolve your issue. Please contact us via<br>
      Brindle if you need assistance.</p>
    </div>
    <div class="back__rule"></div>
    <h2 class="back__headline">WE WOULD LOVE TO<br>HEAR YOUR FEEDBACK!</h2>
  </section>

</main>
</body>
</html>
```